依頼詳細
このチラシは 2月中旬に公的な機関(駅・市役所・市の施設)を中心に設置します。本法人のウェブサイトにもアップいたします。
記載項目
社名:あおばねオンライン寺子屋(個別学習指導)
℡番号:03-5817-2240
URL:https://verdalo-kanto.jp
QRコードを作成お願いいたします。
ロゴマークは添付しております。
キャッチコピー:「いっでんそばにおっでな!」…I'll come and stay with you at any time.の鹿児島弁です。
サイズ
A4
ページ数
片面
希望イメージ
シンプル 複雑
単色 カラフル
暗い 明るい
日常 高級
遊び心 厳粛
未来的 伝統的
女性的 男性的
希望する色
赤系、青系
納品ファイル
• 高解像度JPG (.jpg)
• イラストレーター形式 (.ai)
補足説明
添付資料「パンフ原稿」pp1-2を参考にしてください。全部使用する必要はありません。
念のために…
主催団体:一般社団法人ヴェルダロ青少年グローバル交流センター
所在地:〒150-0093 東京都渋谷区桐ケ丘3-8-24-402
はロゴマーク、QRコード、URL、e-mail アドレスなどとともに記載必須です。

重要事項…インターネット環境とパソコンさえあれば受講できます。
体験授業は3月から随時。4月から本格的に授業開始。
参加ご希望者はウェブサイトよりお申し込みください。
作品ご応募を検討される皆様へ
チラシをラックに置くことも考慮し、タイトルの「青羽オンライン寺子屋(個別学習)」をチラシ上部にデザインしていただきますようお願いいたします。
■ 選んだ理由

当選された方には まだ修正していただくことがございますが 笑顔の少年のイメージが弊社の考えていたイメージにマッチしていたことです。弊社の希望する色遣いの赤・青とは異なっていましたが それを差し引いても 随所に出品者様の工夫やご提案がありました。こういう姿勢も大切かと思いました。

■ 提案者全員のお礼・コメント

短期間に甲乙つけがたい作品が14作品も結集いたしましたことを心より御礼申し上げます。いつもそうですが 1つに絞ることを心苦しく思います。お許しください。遠隔地の教育に力を入れたいという弊社の取り組みに300名を超える方の閲覧を受け さらにはご応募いただきましたことを重ねてお礼申し上げます。

```html
<!DOCTYPE html>
<html lang="ja">
<head>
<meta charset="UTF-8">
<title>あおばねオンライン寺子屋 個別学習指導</title>
<link href="https://fonts.googleapis.com/css2?family=Noto+Sans+JP:wght@400;500;700;900&family=M+PLUS+Rounded+1c:wght@700;800&display=swap" rel="stylesheet">
<style>
:root{
  --green:#3a9a3c;
  --green-light:#8cc63f;
  --navy:#1c3f8f;
  --orange:#f08a1c;
  --ink:#333;
  --paper:#ffffff;
  --photo-a:#d9e6ef;
  --photo-b:#b9c9d4;
}
*{margin:0;padding:0;box-sizing:border-box}
html,body{width:848px;height:1200px;overflow:hidden;background:var(--paper)}
body{font-family:"Noto Sans JP",sans-serif;color:var(--ink);position:relative}
.flyer{position:relative;width:848px;height:1200px;overflow:hidden}

.catch{position:absolute;top:16px;left:0;width:500px;text-align:center;font-family:"M PLUS Rounded 1c",sans-serif;font-weight:800;font-size:30px;color:var(--green)}
.title-bar{position:absolute;top:62px;left:30px;display:flex;align-items:center;gap:10px}
.title-name{background:var(--green);color:#fff;font-weight:900;font-size:32px;padding:4px 18px;border-radius:4px}
.title-sub{border:2px solid var(--green);color:var(--green);font-weight:700;font-size:24px;padding:4px 12px}

.hero-photo{position:absolute;top:120px;left:330px;width:518px;height:412px;background:linear-gradient(160deg,var(--photo-a),var(--photo-b))}
.tutor-photo{position:absolute;top:400px;left:50px;width:170px;height:115px;background:linear-gradient(160deg,#e8eef4,#aebccb);border:3px solid #fff}
.vertical-note{position:absolute;top:135px;right:30px;writing-mode:vertical-rl;font-size:18px;font-weight:700;color:var(--navy);letter-spacing:2px}

.headline{position:absolute;top:140px;left:34px;color:var(--navy);font-weight:900;line-height:1.15}
.headline .l1{font-size:54px}
.headline .l1 small{font-size:34px}
.headline .tag{display:block;font-size:15px;font-weight:700;margin:10px 0 0 170px;color:var(--navy)}
.headline .l2{font-size:76px;display:block}
.headline .l3{font-size:62px;display:block}

.band{position:absolute;top:532px;left:0;width:848px;height:86px;background:linear-gradient(90deg,var(--green),var(--green-light));color:#fff;font-weight:900;font-size:28px;line-height:1.3;display:flex;align-items:center;padding-left:40px}

.intro{position:absolute;top:636px;left:36px;width:380px;font-size:11.5px;line-height:1.75}
.intro p{margin-bottom:8px}

.start-badge{position:absolute;top:640px;left:450px;width:130px;height:130px;border-radius:50%;background:var(--orange);color:#fff;display:flex;flex-direction:column;align-items:center;justify-content:center;font-weight:900;text-align:center}
.start-badge .big{font-size:32px;line-height:1}
.start-badge .sm{font-size:15px;line-height:1.3}
.trial{position:absolute;top:645px;left:600px;width:210px;border:3px solid var(--orange);color:var(--orange);text-align:center;font-weight:900;padding:10px 6px;background:#fff}
.trial .a{font-size:22px}
.trial .b{font-size:34px;line-height:1.1}
.trial .c{font-size:18px}

.qa{position:absolute;top:785px;left:430px;width:190px;font-size:11px;line-height:1.6}
.qa h3,.merits h3{color:var(--orange);font-size:13px;font-weight:900;margin:0 0 4px;white-space:nowrap}
.qa p{margin-bottom:10px}
.merits{position:absolute;top:785px;left:632px;width:196px;font-size:11px;line-height:1.5}
.merits li{list-style:none;display:flex;gap:4px;margin-bottom:8px;font-weight:700}
.merits li svg{flex:none;margin-top:2px}
.merits li span small{display:block;font-weight:400}

.apply{position:absolute;top:1018px;left:30px;width:788px;height:48px;display:flex;align-items:center;justify-content:space-between}
.apply-note{border:2px solid var(--green);border-radius:24px;font-size:14px;font-weight:700;color:var(--green);padding:8px 18px;white-space:nowrap}
.apply-url{font-size:30px;font-weight:900;color:var(--green);white-space:nowrap}

.footer{position:absolute;top:1075px;left:0;width:848px;height:125px;border-top:4px solid var(--green);padding:12px 30px;display:flex;gap:22px;align-items:center}
.org-mark{display:flex;align-items:center;gap:8px;color:var(--navy);font-weight:900;font-size:26px}
.org-mark i{display:block;width:32px;height:32px;border-radius:50%;background:var(--navy)}
.org-info{flex:1;font-size:12.5px;line-height:1.6}
.org-info .name{font-weight:700;font-size:15px}
.org-info .tel{font-size:28px;font-weight:900;color:var(--navy);display:flex;align-items:center;gap:6px}
.org-info .tel small{font-size:12px;font-weight:500;color:var(--ink)}
.qr{flex:none;width:90px;height:90px;border:3px solid var(--ink);background:#fff}
</style>
</head>
<body>
<div class="flyer">
  <div class="catch">いっでんそばにおっでな!</div>
  <div class="title-bar">
    <div class="title-name">あおばねオンライン寺子屋</div>
    <div class="title-sub">個別学習指導</div>
  </div>

  <div class="hero-photo" role="img" aria-label="パソコンの前で笑顔を見せる少年の写真"></div>
  <div class="vertical-note">自宅で高品質な授業が受けられます!</div>

  <div class="headline">
    <span class="l1">東大生<small>が中心の</small></span>
    <span class="tag">テレビ会議システム</span>
    <span class="l2">オンライン</span>
    <span class="l3">個別学習指導。</span>
  </div>
  <div class="tutor-photo" role="img" aria-label="画面越しに指導する講師の写真"></div>

  <div class="band">インターネット環境とパソコンさえ<br>あれば受講できます。</div>

  <div class="intro">
    <p>青羽オンライン寺子屋は、離れた地域に住む子どもたちにも質の高い学びを届けるため、東大生を中心とした講師陣がテレビ会議システムで一人ひとりに合わせた個別指導を行います。</p>
    <p>学校の授業の復習から受験対策まで、生徒の理解度や目標に合わせて学習計画を立てます。わからないところをその場で質問できるので、苦手をそのままにしません。</p>
    <p>講師は勉強だけでなく、進路や将来についての相談にも応じます。身近な先輩として、学ぶ楽しさや挑戦する気持ちを伝えていきます。</p>
    <p>まずはお気軽に体験授業にご参加ください。保護者の方のご相談も随時受け付けております。</p>
  </div>

  <div class="start-badge"><span class="big">4月〜</span><span class="sm">本格的に<br>授業開始</span></div>
  <div class="trial"><div class="a">体験授業</div><div class="b">3月〜</div><div class="c">随時受付</div></div>

  <div class="qa">
    <h3>オンライン寺子屋の授業とは?</h3>
    <p>カメラとマイクを使い、講師と生徒が画面越しに顔を合わせて学ぶ授業です。資料や問題を共有しながら進めます。</p>
    <h3>オンライン寺子屋授業どんな感じ?</h3>
    <p>1回の授業は約60分。生徒の進み具合を確認しながら、丁寧に解説と演習を繰り返します。</p>
  </div>

  <div class="merits">
    <h3>オンラインを利用するメリットは?</h3>
    <ul>
      <li><svg width="14" height="14" viewBox="0 0 14 14"><path d="M2 7l3 3 7-7" fill="none" stroke="#3a9a3c" stroke-width="2.5"/></svg><span>1 パソコンがあれば自宅で受講できる<small>通塾の時間や送迎が必要ありません。</small></span></li>
      <li><svg width="14" height="14" viewBox="0 0 14 14"><path d="M2 7l3 3 7-7" fill="none" stroke="#3a9a3c" stroke-width="2.5"/></svg><span>2 地方にいても質の高い授業が受けられる<small>距離に関係なく学べます。</small></span></li>
      <li><svg width="14" height="14" viewBox="0 0 14 14"><path d="M2 7l3 3 7-7" fill="none" stroke="#3a9a3c" stroke-width="2.5"/></svg><span>3 好きな時間に授業を受けられる<small>部活や習い事とも両立できます。</small></span></li>
    </ul>
  </div>

  <div class="apply">
    <div class="apply-note">参加ご希望者はウェブサイトよりお申し込みください</div>
    <div class="apply-url">https://verdalo-kanto.jp</div>
  </div>

  <div class="footer">
    <div class="org-mark"><i></i>Verdalo</div>
    <div class="org-info">
      <div class="name">一般社団法人ヴェルダロ青少年グローバル交流センター</div>
      <div class="tel"><svg width="24" height="24" viewBox="0 0 24 24"><path d="M6 2l4 4-2 3c1 3 4 6 7 7l3-2 4 4-3 4C10 22 2 14 2 5z" fill="#1c3f8f"/></svg>03-5817-2240<small>受付時間 平日10:00〜18:00</small></div>
      <div>〒150-0093 東京都渋谷区桐ケ丘3-8-24-402 ／ E-mail: info@verdalo-kanto.jp</div>
    </div>
    <div class="qr" role="img" aria-label="ウェブサイトへのQRコード"></div>
  </div>
</div>
</body>
</html>
```